Bright Polish Leaflet Campaign

We require an eye catching double sided leaflet which is for residential properties as a marketing tool to gain more business.
If you look at our website www.brightpolishcollective.com then it may help you with more information of what we are about.

We require one side of the leaflet for our (Domestic Cleaning) Services, then the other side of the leaflet for our (Carpet and Upholstery Cleaning) Service.

The Domestic Cleaning Service Side: The services we offer are weekly, fortnightly, monthly. One Off Deep Cleans. Holiday cover provided. We also have a comprehensive insurance. You may want to use our company bullet point provided in pdf which will make it stand out and outline what we do e.g.:
-Weekly, fortnightly and Monthly Cleaning Service
-Deep Blitz Cleaning
-Covered by a Comprehensive Insurance
-Carpet and Upholstery Cleaning (see overleaf)

The Carpet and Upholstery Cleaning on the other side of the leaflet has to be eye catching!

Again use bullet points along the lines of:
-Stain Removal Specialists
-Quick Drying Time
-Fresh Deodorising Finish
-Eco Friendly

Both sides of the leaflet need a call to action eg. Call Today! Our company Telephone number which should be on the leaflet in bold is 01904 782 619 .The company email which should aslo be on there is info@brightpolishuk.co.uk and the website which is not live yet is www.brightpolishuk.co.uk. If you would like to add our company accreditations they are on the website and I have attached them also.

Target Market(s)

Domestic Households- Middle aged people In York United Kingdom

Industry/Entity Type

House Cleaning

Font styles to use
Serif
Sans Serif

Requirements
Must have
• -1 Side about Domestic Cleaning Services
• -1 Side about Carpet and Upholstery Cleaning
• -Bullet points with key points
• -Phone number/website/email address
• -Logo
Nice to have
• -BE CREATIVE, USE YOUR IMAGINATION AND CREATE EYE CATCHING MATERIAL.
• -Nice to have a background colour which goes nicely with the logo our company.
Should not have
• -Not to have pink in the leaflet or yellow as it doesn't show up well I don't believe. Up to the designer as I like to give you freedom to create something amazing.

```html
<!DOCTYPE html>
<html lang="en">
<head>
<meta charset="utf-8">
<title>Bright Polish Leaflet</title>
<link href="https://fonts.googleapis.com/css2?family=Arimo:wght@400;700&family=Roboto+Condensed:wght@300;400;700&family=Saira+Semi+Condensed:wght@500;600&display=swap" rel="stylesheet">
<style>
:root{
  --blue:#1d9ad8;
  --blue-deep:#0b74b5;
  --blue-pale:#e6f1f9;
  --ink:#2a2a2a;
  --grey:#5d6166;
  --bubble:#6d7177;
  --page:#ececec;
  --white:#ffffff;
  --badge:#2a3f8f;
}
*{margin:0;padding:0;box-sizing:border-box}
html,body{width:1200px;height:800px;overflow:hidden;background:var(--page)}
.canvas{position:relative;width:1200px;height:800px}
.leaflet{position:absolute;top:38px;width:643px;height:910px;background:var(--white);transform:scale(0.8);transform-origin:0 0;overflow:hidden;box-shadow:0 4px 14px rgba(0,0,0,.25);font-family:"Roboto Condensed",Arial,sans-serif;color:var(--ink)}
.leaflet--domestic{left:64px}
.leaflet--carpet{left:622px}
.leaflet__art{position:absolute;left:0;top:0}
.social{position:absolute;top:16px;right:26px;display:flex;align-items:center;gap:5px;font:700 10px "Arimo",sans-serif;color:var(--white)}
.social__dot{width:29px;height:29px;border-radius:50%;background:var(--blue-deep)}
.social .label{margin-right:4px}
.brand{position:absolute;left:32px;top:20px;width:190px;height:190px;border-radius:50%;background:var(--white);border:6px solid #d8dde2;box-shadow:0 3px 10px rgba(0,0,0,.3);display:flex;align-items:center;justify-content:center;text-align:center}
.brand__name{font:700 30px/1.02 "Arimo",sans-serif;color:var(--blue)}
.hero-title{position:absolute;left:38px;top:257px;height:31px;background:rgba(20,20,20,.88);color:var(--white);font:500 29px/31px "Saira Semi Condensed",sans-serif;padding:0 7px;white-space:nowrap;transform:skewX(-8deg);transform-origin:left}
.hero-sub{position:absolute;left:38px;top:291px;height:47px;background:rgba(29,154,216,.82);color:var(--white);font:500 19px/20px "Saira Semi Condensed",sans-serif;padding:4px 8px;white-space:nowrap}
.photo-tag{position:absolute;left:320px;top:444px;font:400 12px/1 "Arimo",sans-serif;color:var(--ink)}
.section-head{position:absolute;left:38px;width:545px;font:700 30px/1 "Roboto Condensed",sans-serif;color:var(--ink);letter-spacing:-.3px;border-bottom:1px solid #c9ccd0;padding-bottom:3px;white-space:nowrap}
.section-head em{font-style:normal;color:var(--blue)}
.intro{position:absolute;left:38px;width:545px;font:400 11.5px/14px "Arimo",sans-serif;color:var(--grey)}
.checklist{position:absolute;list-style:none;background:var(--blue-pale)}
.checklist li{position:relative;color:var(--grey)}
.tick{position:absolute;left:0;top:0}
.checklist--small{left:38px;top:607px;width:145px;height:205px;padding:17px 3px 0 6px}
.checklist--small li{font:400 11.5px/14px "Arimo",sans-serif;padding-left:13px;margin-bottom:14px}
.checklist--small .tick{width:13px;height:11px;left:0;top:1px}
.price{position:absolute;top:607px;height:207px;border:2px solid var(--blue);border-radius:4px;overflow:hidden;text-align:center}
.price__head{height:76px;background:var(--white)}
.price__tier{font:400 16px/1 "Arimo",sans-serif;color:var(--grey);padding-top:8px}
.price__amount{font:700 38px/1 "Arimo",sans-serif;color:var(--blue);margin-top:3px}
.price__min{font:400 11px/1 "Arimo",sans-serif;color:var(--blue);margin-top:1px}
.price__body{height:131px;background:linear-gradient(var(--blue-deep),var(--blue));color:var(--white);font:700 10.5px/14.3px "Arimo",sans-serif;padding-top:5px;white-space:nowrap}
.price__body u{text-decoration:none;border-bottom:1px solid rgba(255,255,255,.7);display:inline-block;padding:0 4px;line-height:13px}
.accred{position:absolute;font:400 14px/1 "Roboto Condensed",sans-serif;color:var(--ink);white-space:nowrap}
.badge,.bubble{position:absolute}
.cta{position:absolute;font:700 20px/21px "Arimo",sans-serif;color:var(--blue)}
.bubble__phone{font:700 22px "Arimo",sans-serif;fill:var(--white)}
.bubble__mail{font:400 10px "Arimo",sans-serif;fill:var(--white)}
.checklist--large{left:37px;top:578px;width:310px;height:149px;padding:17px 0 0 33px}
.checklist--large li{font:400 16.5px/17px "Roboto Condensed",sans-serif;padding-left:44px;margin-bottom:17px;color:var(--ink)}
.checklist--large .tick{width:32px;height:22px;top:-3px}
.side-copy{position:absolute;left:363px;top:605px;width:240px;font:400 11.5px/14px "Arimo",sans-serif;color:var(--grey)}
</style>
</head>
<body>
<div class="canvas">

  <article class="leaflet leaflet--domestic">
    <svg class="leaflet__art" width="643" height="910" viewBox="0 0 643 910">
      <defs>
        <linearGradient id="skyA" x1="0" y1="0" x2="0" y2="1"><stop offset="0" stop-color="#0b74b5"/><stop offset="1" stop-color="#3fb3e8"/></linearGradient>
        <linearGradient id="photoA" x1="0" y1="0" x2="1" y2="1"><stop offset="0" stop-color="#6f767c"/><stop offset=".5" stop-color="#aeb4b9"/><stop offset="1" stop-color="#d8c8b6"/></linearGradient>
        <linearGradient id="swooshA" x1="0" y1="0" x2="1" y2="0"><stop offset="0" stop-color="#4e5257"/><stop offset="1" stop-color="#8f959b"/></linearGradient>
        <linearGradient id="fadeA" x1="0" y1="0" x2="0" y2="1"><stop offset="0" stop-color="#b9bcc0"/><stop offset="1" stop-color="#ffffff"/></linearGradient>
      </defs>
      <rect width="643" height="270" fill="url(#skyA)"/>
      <path d="M0,210 C180,120 420,100 643,88 L643,300 C480,300 260,330 0,430 Z" fill="url(#photoA)" role="img" aria-label="Photo of a hand vacuuming a grey upholstered sofa"/>
      <path d="M0,430 C260,330 480,300 643,300 L643,430 C430,420 220,460 0,520 Z" fill="url(#swooshA)"/>
      <path d="M0,520 C220,460 430,420 643,430 L643,612 L0,612 Z" fill="url(#fadeA)" role="img" aria-label="Faded photo of a cleaner wiping a surface"/>
    </svg>
    <div class="social"><span class="label">Follow Us :</span><span class="social__dot"></span><span class="social__dot"></span><span class="social__dot"></span></div>
    <div class="brand"><span class="brand__name">Bright<br>Polish</span></div>
    <div class="hero-title">DOMESTIC CLEANING SERVICES</div>
    <div class="hero-sub">Enjoy A Clean Home At<br>An Affordable Price</div>
    <div class="photo-tag">Eco friendly</div>

    <h2 class="section-head" style="top:515px">DOMESTIC <em>CLEANING SERVICES</em></h2>
    <p class="intro" style="top:546px">The services we offer are weekly, fortnightly, monthly. One Off Deep Cleans. Holiday cover provided. We also have a comprehensive insurance. You may want to use our company bullet point provided in pdf which will make it stand out and outline what we do e.g.:</p>

    <ul class="checklist checklist--small">
      <li><svg class="tick" viewBox="0 0 14 12"><path d="M1,6 L5,10 L13,1" fill="none" stroke="#1d9ad8" stroke-width="2.4"/></svg>Weekly, fortnightly and Monthly Cleaning Service</li>
      <li><svg class="tick" viewBox="0 0 14 12"><path d="M1,6 L5,10 L13,1" fill="none" stroke="#1d9ad8" stroke-width="2.4"/></svg>Deep Blitz Cleaning</li>
      <li><svg class="tick" viewBox="0 0 14 12"><path d="M1,6 L5,10 L13,1" fill="none" stroke="#1d9ad8" stroke-width="2.4"/></svg>Covered by a Comprehensive Insurance</li>
      <li><svg class="tick" viewBox="0 0 14 12"><path d="M1,6 L5,10 L13,1" fill="none" stroke="#1d9ad8" stroke-width="2.4"/></svg>Carpet and Upholstery Cleaning (see overleaf)</li>
    </ul>

    <section class="price" style="left:193px;width:132px">
      <div class="price__head"><div class="price__tier">STANDARD</div><div class="price__amount">£24</div><div class="price__min">2 hours minimum</div></div>
      <div class="price__body">Vacuum and clean<br>carpets and floors<br>Dust down services<br>Empty bins<br><u>Hygiene Clean of:</u><br>✓ Kitchen<br>✓ Bathroom<br>✓ Toilet</div>
    </section>
    <section class="price" style="left:342px;width:130px">
      <div class="price__head"><div class="price__tier">PREMIUM</div><div class="price__amount">£36</div><div class="price__min">2 hours minimum</div></div>
      <div class="price__body">As Standard Plus:<br>3 Hours Minimum<br>Interior Windows<br><u>Deep Clean:</u><br>✓ Kitchen<br>✓ Bathroom<br>✓ Toilet</div>
    </section>
    <section class="price" style="left:486px;width:131px">
      <div class="price__head"><div class="price__tier">STANDARD</div><div class="price__amount">£50</div><div class="price__min">2 hours minimum</div></div>
      <div class="price__body">As Premium Plus:<br>4 Hours Minimum<br>Furniture Polishing<br>Skirting Boards and<br>Coving<br>Flowers and Freshners</div>
    </section>

    <div class="accred" style="left:44px;top:856px">ACCREDITATIONS</div>
    <svg class="badge" style="left:158px;top:832px" width="64" height="64" viewBox="0 0 64 64" role="img" aria-label="Safety contractor accreditation badge"><circle cx="32" cy="32" r="30" fill="#fff" stroke="#2a3f8f" stroke-width="3"/></svg>
    <svg class="badge" style="left:238px;top:836px" width="76" height="56" viewBox="0 0 76 56" role="img" aria-label="Health and safety scheme accreditation badge"><rect x="2" y="2" width="72" height="52" rx="6" fill="#2a3f8f"/></svg>

    <div class="cta" style="left:342px;top:826px">CALL<br>TODAY!</div>
    <svg class="bubble" style="left:385px;top:812px" width="230" height="96" viewBox="0 0 230 96">
      <path d="M2,90 L60,66 L80,84 Z" fill="#6d7177"/>
      <g transform="rotate(-10 128 50)">
        <ellipse cx="128" cy="50" rx="100" ry="38" fill="#6d7177"/>
        <text class="bubble__phone" x="128" y="47" text-anchor="middle">01904 782 619</text>
        <text class="bubble__mail" x="128" y="62" text-anchor="middle">info@brightpolishuk.co.uk</text>
        <text class="bubble__mail" x="128" y="74" text-anchor="middle">www.brightpolishuk.co.uk</text>
      </g>
    </svg>
  </article>

  <article class="leaflet leaflet--carpet">
    <svg class="leaflet__art" width="643" height="910" viewBox="0 0 643 910">
      <defs>
        <linearGradient id="skyB" x1="0" y1="0" x2="0" y2="1"><stop offset="0" stop-color="#0b74b5"/><stop offset="1" stop-color="#3fb3e8"/></linearGradient>
        <linearGradient id="photoB" x1="0" y1="0" x2="1" y2="1"><stop offset="0" stop-color="#8c9094"/><stop offset=".6" stop-color="#c4c7c9"/><stop offset="1" stop-color="#9a9ea2"/></linearGradient>
        <linearGradient id="swooshB" x1="0" y1="0" x2="1" y2="0"><stop offset="0" stop-color="#4e5257"/><stop offset="1" stop-color="#8f959b"/></linearGradient>
        <linearGradient id="fadeB" x1="0" y1="0" x2="0" y2="1"><stop offset="0" stop-color="#b9bcc0"/><stop offset="1" stop-color="#ffffff"/></linearGradient>
      </defs>
      <rect width="643" height="270" fill="url(#skyB)"/>
      <path d="M0,210 C180,120 420,100 643,88 L643,300 C480,300 260,330 0,430 Z" fill="url(#photoB)" role="img" aria-label="Photo of a vacuum head on a light grey carpet"/>
      <path d="M0,430 C260,330 480,300 643,300 L643,430 C430,420 220,460 0,520 Z" fill="url(#swooshB)"/>
      <path d="M0,520 C220,460 430,420 643,430 L643,612 L0,612 Z" fill="url(#fadeB)" role="img" aria-label="Faded photo of a cleaner wiping a surface"/>
    </svg>
    <div class="social"><span class="label">Follow Us :</span><span class="social__dot"></span><span class="social__dot"></span><span class="social__dot"></span></div>
    <div class="brand"><span class="brand__name">Bright<br>Polish</span></div>
    <div class="hero-title" style="left:40px">CARPET AND UPHOLSTERY CLEANING</div>
    <div class="hero-sub" style="left:40px">Why You Need Your Carpets<br>And Upholstery To Be Clean</div>

    <h2 class="section-head" style="top:512px">DOMESTIC <em>CLEANING SERVICES</em></h2>
    <p class="intro" style="top:543px">The benefits you will reap from our Domestic Carpet Cleaning Service will be paramount.</p>

    <ul class="checklist checklist--large">
      <li><svg class="tick" viewBox="0 0 32 22"><path d="M2,12 L11,20 L30,2" fill="none" stroke="#1d9ad8" stroke-width="4"/></svg>Stain Removal Specialists</li>
      <li><svg class="tick" viewBox="0 0 32 22"><path d="M2,12 L11,20 L30,2" fill="none" stroke="#1d9ad8" stroke-width="4"/></svg>Quick Drying Time</li>
      <li><svg class="tick" viewBox="0 0 32 22"><path d="M2,12 L11,20 L30,2" fill="none" stroke="#1d9ad8" stroke-width="4"/></svg>Fresh Deodorising Finish</li>
      <li><svg class="tick" viewBox="0 0 32 22"><path d="M2,12 L11,20 L30,2" fill="none" stroke="#1d9ad8" stroke-width="4"/></svg>Eco friendly</li>
    </ul>
    <p class="side-copy">Heavy usage of carpets can lead to carpet fibres becoming soiled, regardless of how often you vacuum them. You will benefit from the services of our professionally trained Carpet Cleaning Staff, who will help you maintain your premises to look professional and keep your carpets staying fresh.</p>

    <div class="accred" style="left:41px;top:759px">ACCREDITATIONS</div>
    <svg class="badge" style="left:45px;top:782px" width="96" height="96" viewBox="0 0 96 96" role="img" aria-label="Safety contractor accreditation badge"><circle cx="48" cy="48" r="45" fill="#fff" stroke="#2a3f8f" stroke-width="4"/></svg>
    <svg class="badge" style="left:160px;top:788px" width="116" height="84" viewBox="0 0 116 84" role="img" aria-label="Health and safety scheme accreditation badge"><rect x="4" y="4" width="108" height="76" rx="8" fill="#2a3f8f"/></svg>

    <div class="cta" style="left:330px;top:770px">CALL<br>TODAY!</div>
    <svg class="bubble" style="left:374px;top:740px" width="250" height="104" viewBox="0 0 230 96">
      <path d="M2,90 L60,66 L80,84 Z" fill="#6d7177"/>
      <g transform="rotate(-10 128 50)">
        <ellipse cx="128" cy="50" rx="100" ry="38" fill="#6d7177"/>
        <text class="bubble__phone" x="128" y="47" text-anchor="middle">01904 782 619</text>
        <text class="bubble__mail" x="128" y="62" text-anchor="middle">info@brightpolishuk.co.uk</text>
        <text class="bubble__mail" x="128" y="74" text-anchor="middle">www.brightpolishuk.co.uk</text>
      </g>
    </svg>
  </article>

</div>
</body>
</html>
```